Verostel business card

Business card for sustainable investment company called "Verostel". Verostel is an exchange platform selling carbon credits between buyers and sellers. Carbon Credits are an environmental commodity for reducing global carbon emissions.

the card should obviously have our logo and the theme should be sustainability/environment mixed with a trading platform.

Contact Information for Business Card

Logo, Name, Title, Phone, Email

Colors
0054AA
0677BA
7BADD7
CADEEF
E8F1F8
0094D4
00A9DD
6FCCEA
C7EBF8
E9F6FB
00AB8E
00BBA5
67D7C9
C6EFE9
E9F9F6
59FF00
82FF00
B8FF75
E3FFCB
F4FFEA

```html
<!DOCTYPE html>
<html lang="en">
<head>
<meta charset="utf-8">
<title>Verostel Business Card</title>
<link href="https://fonts.googleapis.com/css2?family=Montserrat:wght@400;500;700&family=Pinyon+Script&display=swap" rel="stylesheet">
<style>
  :root {
    --backdrop: #c6c7c9;
    --card-stock: #efeee8;
    --ink-navy: #1b2a52;
    --edge-teal: #22a9cf;
    --accent-blue: #0677BA;
    --accent-light: #6FCCEA;
  }
  html, body {
    margin: 0;
    padding: 0;
    width: 1200px;
    height: 1050px;
    overflow: hidden;
    background: var(--backdrop);
    font-family: "Montserrat", sans-serif;
  }
  .canvas {
    position: relative;
    width: 1200px;
    height: 1050px;
  }
  .card {
    position: absolute;
    width: 600px;
    height: 343px;
    background: var(--card-stock);
    border-bottom: 6px solid var(--edge-teal);
    box-sizing: border-box;
  }
  .card--back {
    left: 520px;
    top: 150px;
    display: flex;
    align-items: center;
    justify-content: center;
  }
  .card--front {
    left: 80px;
    top: 560px;
    display: flex;
    flex-direction: column;
    align-items: center;
    padding-top: 46px;
  }
  .brand {
    display: flex;
    align-items: center;
    gap: 14px;
    color: var(--ink-navy);
    font-weight: 700;
    letter-spacing: 0.04em;
  }
  .brand__square {
    width: 44px;
    height: 44px;
    background: linear-gradient(135deg, var(--accent-light), var(--accent-blue));
  }
  .card--back .brand { font-size: 46px; }
  .card--front .brand { font-size: 22px; }
  .card--front .brand__square { width: 28px; height: 28px; }
  .holder__name {
    margin-top: 34px;
    font-size: 30px;
    font-weight: 700;
    letter-spacing: 0.12em;
    color: var(--ink-navy);
  }
  .holder__title {
    font-family: "Pinyon Script", cursive;
    font-size: 20px;
    color: var(--ink-navy);
    margin-top: 2px;
  }
  .contact {
    margin-top: 22px;
    text-align: center;
    font-size: 15px;
    font-weight: 500;
    letter-spacing: 0.22em;
    text-transform: uppercase;
    color: var(--ink-navy);
    line-height: 1.8;
  }
  .contact__divider {
    color: var(--accent-blue);
    padding: 0 6px;
  }
</style>
</head>
<body>
  <div class="canvas">
    <section class="card card--back">
      <div class="brand"><span class="brand__square"></span>VEROSTEL</div>
    </section>

    <section class="card card--front">
      <div class="brand"><span class="brand__square"></span>VEROSTEL</div>
      <div class="holder__name">MARCUS HALE</div>
      <div class="holder__title">Founder</div>
      <div class="contact">
        <div>www.verostel.com<span class="contact__divider">|</span>303-555-0147</div>
        <div>info@verostel.com</div>
      </div>
    </section>
  </div>
</body>
</html>
```